Modern Retail Coffee Label for established Roastery! 17 years!

We are looking for a Retail Coffee Bag Label... JUST THE LABEL TO GO ON AN EXISTING BAG. Our current label is provided and our Logo.. we have had the same Red Bags FOREVER so we are looking for a label to compliment that tradition and to be placed on the bags we have used for 17 years.

We have a retail line of bags with locally roasted coffee. Our business has been around 17years and is in need of a design upgrade! We have a red coffee bag and are looking for a sleek modern label. I will attach a file of our label right now so you can see what it looks like. We are just looking for a more modern version. a few inclusions:

Locally Roasted
100% Arabica Coffee
Heron Kin's Coffee
heronkincoffee.example
logo

The black label with the red and yellow color label is the old one... the new label should be the White background and black border one...

Target Market(s)

Retail Coffee Consumers

Font styles to use
Other font styles liked:
• use what you think. we are located in SW Wisconsin but ship coffee EVERYWHERE

Colors

Designer to choose only greyscale colors for use in the design.

Requirements
Must have
• Locally Roasted (Platteville,WI)
• 100% Arabica Coffee
• heronkincoffee.example
• logo
Nice to have
• Badgers
• "Since 2003"
Should not have
• Any lunabrew or big brand themes

```html
<!DOCTYPE html>
<html lang="en">
<head>
<meta charset="utf-8">
<title>Heron Kin's Coffee – Retail Bag Label</title>
<link rel="stylesheet" href="https://fonts.googleapis.com/css2?family=Oswald:wght@700&family=Fira+Sans:wght@600&display=swap">
<style>
  :root {
    --stage: #5a0006;
    --stage-edge: #2a0003;
    --ink: #000000;
    --paper: #ffffff;
    --gold: #d9b66f;
    --cream: #f1ddb0;
    --wash-dark: #8a7f72;
    --wash-mid: #b3a897;
    --wash-light: #e2dbd0;
  }
  * { margin: 0; padding: 0; box-sizing: border-box; }
  html, body { width: 1200px; height: 839px; overflow: hidden; }
  body {
    background: radial-gradient(ellipse at 50% 45%, var(--stage) 0%, var(--stage-edge) 100%);
    position: relative;
    font-family: "Fira Sans", "Helvetica Neue", Arial, sans-serif;
  }
  .label {
    position: absolute;
    left: 280px; top: 20px;
    width: 640px; height: 800px;
    background: var(--ink);
  }
  .label__art {
    position: absolute;
    left: 15px; top: 17px;
    width: 610px; height: 707px;
    background:
      radial-gradient(ellipse at 30% 70%, var(--wash-light) 0%, transparent 45%),
      radial-gradient(ellipse at 80% 35%, var(--wash-light) 0%, transparent 40%),
      linear-gradient(160deg, var(--wash-mid) 0%, var(--wash-dark) 55%, var(--wash-mid) 100%);
    clip-path: polygon(0 0, 100% 0, 100% 100%, 50% 98.6%, 0 100%);
  }
  .label__shapes { position: absolute; inset: 0; }
  .label__tagline {
    position: absolute;
    left: 175px; width: 291px; top: 40px;
    text-align: center;
    color: var(--cream);
    font-size: 30px;
    line-height: 1;
  }
  .label__brand {
    position: absolute;
    left: 111px; top: 92px;
    width: 416px; height: 231px;
    background: var(--paper);
    border: 7px solid var(--ink);
    border-radius: 12px;
    display: flex; flex-direction: column;
    align-items: center; justify-content: center;
    gap: 6px;
    font-family: "Oswald", "Arial Narrow", sans-serif;
    font-weight: 700;
    color: var(--ink);
    text-transform: uppercase;
    line-height: 1;
  }
  .label__brand-name { font-size: 66px; letter-spacing: 2px; }
  .label__brand-word { font-size: 66px; letter-spacing: 3px; }
  .label__since {
    position: absolute;
    left: 175px; width: 291px; top: 338px;
    text-align: center;
    color: var(--cream);
    font-size: 21px;
    line-height: 1;
  }
  .label__seal {
    position: absolute;
    left: 428px; top: 526px;
    width: 190px; height: 190px;
  }
  .label__web {
    position: absolute;
    left: 0; right: 0; top: 741px;
    text-align: center;
    color: var(--cream);
    font-size: 33px;
    line-height: 1;
  }
</style>
</head>
<body>
  <div class="label">
    <div class="label__art" role="img" aria-label="Soft sepia watercolour wash texture in warm greys and off-white"></div>

    <svg class="label__shapes" width="640" height="800" viewBox="0 0 640 800" aria-hidden="true">
      <polygon points="175,17 466,17 466,406 320,380 175,406" fill="var(--ink)"/>
      <line x1="185" y1="17" x2="185" y2="92" stroke="var(--gold)" stroke-width="2"/>
      <line x1="456" y1="17" x2="456" y2="92" stroke="var(--gold)" stroke-width="2"/>
      <polyline points="185,323 185,395 320,371 456,395 456,323" fill="none" stroke="var(--gold)" stroke-width="2"/>
    </svg>

    <div class="label__tagline">Locally Roasted</div>

    <div class="label__brand">
      <span class="label__brand-name">Heron Kin's</span>
      <span class="label__brand-word">Coffee</span>
    </div>

    <div class="label__since">SINCE 2003</div>

    <svg class="label__seal" viewBox="0 0 190 190">
      <circle cx="95" cy="95" r="82" fill="var(--ink)"/>
      <circle cx="95" cy="95" r="84" fill="none" stroke="var(--ink)" stroke-width="14" stroke-linecap="round" stroke-dasharray="0 13.19"/>
      <circle cx="95" cy="95" r="70" fill="none" stroke="var(--gold)" stroke-width="2"/>
      <g transform="rotate(18 95 95)" fill="var(--cream)" font-family="Fira Sans, Arial, sans-serif" font-weight="600" text-anchor="middle">
        <text x="95" y="78" font-size="34">100%</text>
        <text x="95" y="108" font-size="30">Arabica</text>
        <text x="95" y="136" font-size="28">Coffee</text>
      </g>
    </svg>

    <div class="label__web">heronkincoffee.example</div>
  </div>
</body>
</html>
```